Marlow Crest Group (Real Estate and Investment)

A high end, clean design.
We are a real estate company with sales, asset management and investment divisions. We want to use a black and white scheme which is really high end feel. The back of the card can just be the logo (black background with the white writing) as we will probably emboss this when we print)

Target Market(s)

High level investors, high end houses for sale

Industry/Entity Type

Business

Contact Information for Business Card

Name, position, phone number and email address
Glen Varley, Managing Director, 0437259064 and glen@marlowcrest-example.com.au

Requirements
Must have
• Back of the card to be the black background with the white writing (as per the attached images). Would like the capacity to emboss the writing and logo

```html
<!DOCTYPE html>
<html lang="en">
<head>
<meta charset="utf-8">
<title>Marlow Crest Group – Business Card</title>
<link rel="stylesheet" href="https://fonts.googleapis.com/css2?family=Arimo:wght@400;700&family=Open+Sans:wght@400&display=swap">
<style>
  :root {
    --backdrop: #b3b3b3;
    --card-white: #ffffff;
    --card-black: #231f20;
    --card-black-soft: #2c2829;
    --ink: #1a1a1a;
    --ink-soft: #333333;
    --rule: #9a9a9a;
    --paper-text: #f2f2f2;
  }
  * { margin: 0; padding: 0; box-sizing: border-box; }
  html, body {
    width: 1200px; height: 900px; overflow: hidden;
    background: var(--backdrop);
  }
  .canvas { position: relative; width: 1200px; height: 900px; }
  .card {
    position: absolute; top: 306px;
    width: 440px; height: 271px;
    border-radius: 12px; overflow: hidden;
  }
  .card--front { left: 149px; background: var(--card-white); }
  .card--back { left: 608px; background: var(--card-black); }

  .brand {
    position: absolute; left: 8px; width: 188px; top: 88px;
    display: flex; flex-direction: column; align-items: center;
  }
  .brand__mark {
    width: 66px; height: 66px; border-radius: 50%;
    border: 1.5px solid var(--ink);
  }
  .brand__name {
    margin-top: 18px;
    font-family: "Arimo", Arial, sans-serif; font-weight: 400;
    font-size: 14px; letter-spacing: 0.1px; color: var(--ink);
    white-space: nowrap;
  }
  .divider {
    position: absolute; left: 205px; top: 92px;
    width: 1px; height: 90px; background: var(--rule);
  }
  .contact { position: absolute; left: 224px; top: 96px; color: var(--ink); }
  .contact__name {
    font-family: "Arimo", Arial, sans-serif; font-size: 17px; line-height: 20px;
    font-weight: 400; letter-spacing: 0.3px;
  }
  .contact__name strong { font-weight: 700; }
  .contact__role {
    font-family: "Open Sans", Arial, sans-serif; font-size: 11px;
    line-height: 15px; color: var(--ink-soft);
  }
  .contact__list { list-style: none; margin-top: 11px; }
  .contact__item {
    display: flex; align-items: center; gap: 3px;
    font-family: "Open Sans", Arial, sans-serif; font-size: 11px;
    line-height: 17px; color: var(--ink-soft); white-space: nowrap;
  }
  .contact__icon { width: 10px; height: 10px; fill: var(--ink); flex: none; }

  .back__pattern {
    position: absolute; inset: 0;
    background: linear-gradient(160deg, var(--card-black-soft), var(--card-black));
  }
  .back__name {
    position: absolute; right: 32px; bottom: 34px;
    font-family: "Arimo", Arial, sans-serif; font-weight: 400;
    font-size: 21px; color: var(--paper-text); letter-spacing: 0.2px;
    white-space: nowrap;
  }
</style>
</head>
<body>
<main class="canvas">
  <section class="card card--front" aria-label="Card front">
    <div class="brand">
      <div class="brand__mark"></div>
      <div class="brand__name">MARLOW CREST GROUP</div>
    </div>
    <div class="divider"></div>
    <div class="contact">
      <div class="contact__name">GLEN <strong>VARLEY</strong></div>
      <div class="contact__role">Managing Director</div>
      <ul class="contact__list">
        <li class="contact__item">
          <svg class="contact__icon" viewBox="0 0 24 24"><path d="M6.6 10.8a15.1 15.1 0 0 0 6.6 6.6l2.2-2.2c.3-.3.7-.4 1-.2 1.1.4 2.3.6 3.6.6.6 0 1 .4 1 1V20c0 .6-.4 1-1 1A17 17 0 0 1 3 4c0-.6.4-1 1-1h3.5c.6 0 1 .4 1 1 0 1.3.2 2.5.6 3.6.1.3 0 .7-.2 1z"/></svg>
          0437259064
        </li>
        <li class="contact__item">
          <svg class="contact__icon" viewBox="0 0 24 24"><path d="M2 5h20v14H2z"/><path d="M3 6l9 6.3L21 6" fill="none" stroke="#fff" stroke-width="1.8"/></svg>
          glen@marlowcrest-example.com.au
        </li>
      </ul>
    </div>
  </section>

  <section class="card card--back" aria-label="Card back">
    <div class="back__pattern" role="img" aria-label="Faint repeating tone-on-tone brand pattern across the black card back"></div>
    <div class="back__name">MARLOW CREST GROUP</div>
  </section>
</main>
</body>
</html>
```